We CARE about Marriage Event

I need a flyer to promote an Event we do that promotes Marriage and asks people to get involved in Ministry to Marriage. I need a graphic with the words: "We TEND to Wedlock!"

Target Market(s)

Potential volunteers to get involve in the marriage ministry in a particular Catholic Parish.

Industry/Entity Type

Ministry

Logo Text

We TEND to Wedlock!

Colors

Designer to choose colors to be used in the design.

Requirements
Must have
• Under the graphic should be the words: "An Event to Encourage and Support Marriages in our Parish"
• There could be a picture or pictures of married couples at different ages/stages.
• Other words include:
• "Please join us as we discuss the realities facing married couples today and what our response as a Parish can and should be."
• I also need a place to put name of Parish, date, time and location. This information will change for each event so the actual information will need to be left blank.
Nice to have
• Please make it eye-catching and something that would like to attend.
• WE hope the logo itself is fun and colorful.
• Would also like our non-profit logo along with the words "Conducted By..."(HearthBond Alliance) somewhere on flyer.

```html
<!DOCTYPE html>
<html lang="en">
<head>
<meta charset="utf-8">
<title>We TEND to Wedlock! – Event Flyer</title>
<link rel="stylesheet" href="https://fonts.googleapis.com/css2?family=Josefin+Sans:wght@300;400;600;700&family=Oswald:wght@400;500&display=swap">
<style>
  :root {
    --backdrop: #3b3733;
    --ink-dark: #1b2d2f;
    --teal: #4f8a90;
    --teal-soft: #7fb0b4;
    --paper: #ffffff;
    --text-light: #ffffff;
    --logo-ink: #1b2d2f;
  }
  * { box-sizing: border-box; margin: 0; padding: 0; }
  html, body {
    width: 1200px;
    height: 1142px;
    overflow: hidden;
    background: var(--backdrop);
  }
  .flyer {
    position: absolute;
    left: 190px;
    top: 41px;
    width: 820px;
    height: 1060px;
    overflow: hidden;
    background: var(--ink-dark);
    box-shadow: 0 10px 30px rgba(0,0,0,0.35);
  }
  .flyer-shapes {
    position: absolute;
    inset: 0;
    width: 820px;
    height: 1060px;
  }
  .title-block {
    position: absolute;
    left: 418px;
    top: 318px;
    width: 390px;
    color: var(--text-light);
  }
  .title-main {
    font-family: "Josefin Sans", sans-serif;
    font-weight: 700;
    font-size: 58px;
    line-height: 1;
    letter-spacing: 1px;
    display: flex;
    align-items: flex-end;
    gap: 8px;
  }
  .title-figure-slot {
    display: inline-block;
    width: 38px;
    height: 62px;
    background: var(--teal-soft);
    opacity: 0.55;
    border-radius: 4px;
  }
  .title-sub {
    font-family: "Josefin Sans", sans-serif;
    font-weight: 300;
    font-size: 35px;
    line-height: 1.1;
    letter-spacing: 1px;
    margin-top: 2px;
  }
  .tagline {
    font-family: "Oswald", sans-serif;
    font-weight: 400;
    font-size: 21px;
    line-height: 1.25;
    color: var(--ink-dark);
    margin-top: 14px;
  }
  .invitation {
    position: absolute;
    left: 34px;
    top: 400px;
    font-family: "Oswald", sans-serif;
    font-weight: 400;
    font-size: 28px;
    line-height: 40px;
    color: var(--text-light);
  }
  .event-details {
    position: absolute;
    left: 48px;
    top: 718px;
    color: var(--text-light);
    font-family: "Josefin Sans", sans-serif;
  }
  .parish-name { font-weight: 600; font-size: 40px; line-height: 1.1; }
  .parish-address { font-weight: 300; font-size: 25px; margin-top: 8px; }
  .event-when {
    position: absolute;
    left: 150px;
    top: 858px;
    color: var(--text-light);
    font-family: "Josefin Sans", sans-serif;
    text-align: center;
  }
  .event-date { font-weight: 600; font-size: 36px; line-height: 1.2; }
  .event-time { font-weight: 300; font-size: 36px; line-height: 1.2; }
  .host-mark {
    position: absolute;
    left: 12px;
    top: 1004px;
    font-family: "Josefin Sans", sans-serif;
    color: var(--logo-ink);
    white-space: nowrap;
  }
  .host-lead { font-size: 9px; font-weight: 400; margin-left: 24px; }
  .host-row { display: flex; align-items: center; gap: 6px; }
  .host-square { width: 18px; height: 18px; background: var(--logo-ink); }
  .host-name { font-size: 13px; font-weight: 400; }
  .host-line { font-size: 8px; font-weight: 400; margin-left: 24px; }
</style>
</head>
<body>
  <main class="flyer">
    <svg class="flyer-shapes" viewBox="0 0 820 1060">
      <defs>
        <linearGradient id="young-couple-tones" x1="0" y1="0" x2="1" y2="1">
          <stop offset="0" stop-color="#c9b39a"/>
          <stop offset="0.5" stop-color="#8c6d58"/>
          <stop offset="1" stop-color="#5a4034"/>
        </linearGradient>
        <linearGradient id="older-couple-tones" x1="0" y1="0" x2="1" y2="1">
          <stop offset="0" stop-color="#dfe6a8"/>
          <stop offset="0.45" stop-color="#d9b9a0"/>
          <stop offset="1" stop-color="#8fbcb3"/>
        </linearGradient>
      </defs>
      <rect class="photo-young-couple" x="0" y="0" width="820" height="1060" fill="url(#young-couple-tones)" role="img" aria-label="Photo of a young couple talking on a sofa"/>
      <polygon class="band-teal" points="580,0 820,0 820,400 480,760 300,540" fill="var(--teal)"/>
      <polygon class="photo-older-couple" points="820,400 480,760 560,1060 820,1060" fill="url(#older-couple-tones)" role="img" aria-label="Photo of a smiling older married couple"/>
      <polygon class="panel-dark" points="0,300 300,540 480,760 560,1060 0,1060" fill="var(--ink-dark)"/>
      <polygon class="corner-white" points="0,860 0,1060 250,1060" fill="var(--paper)"/>
    </svg>

    <header class="title-block">
      <h1 class="title-main">WE <span class="title-figure-slot" role="img" aria-label="Line drawing of a bride and groom"></span> TEND</h1>
      <p class="title-sub">TO WEDLOCK!</p>
      <p class="tagline">An Event to Encourage and<br>Support Marriages in our Parish</p>
    </header>

    <p class="invitation">
      Please<br>
      join us as<br>
      we discuss the<br>
      realities facing<br>
      married couples today<br>
      and what our response as<br>
      a Parish can and should be.
    </p>

    <section class="event-details">
      <p class="parish-name">Name of Parish</p>
      <p class="parish-address">5134 West Anydrive, Anytown</p>
    </section>

    <section class="event-when">
      <p class="event-date">November 30, 2017</p>
      <p class="event-time">3:00-5:00pm</p>
    </section>

    <footer class="host-mark">
      <p class="host-lead">Conducted By...</p>
      <div class="host-row">
        <span class="host-square"></span>
        <span class="host-name">HearthBond Alliance</span>
      </div>
      <p class="host-line">Serving Parish Families</p>
    </footer>
  </main>
</body>
</html>
```